Harbor Nightclub

Nightclub flyer., digital single sided, for KV and PX. I included samples of some previous flyers we've used. Sample Info:
HARBOR
FRIDAYS
FRI MAY 1 2020
DJ VORTAN (club floor)
DJ RUZO & DJ TAV (residents on the lounge floor)
4217 Marlow Avenue Sacramento
www.harborvenuehall.example for list/VIP inquiries

Target Market(s)

Upscale top 40 crowd but want some cool and artsy like the examples included.

Font styles to use
Sans Serif

Requirements
Must have
• Harbor Logo
Nice to have
• Would be nice if the flyer can be incorporated later with DJ photos (sometimes we will add dj photos to pixagram etc). Would like a big city type of feel.
Should not have
• Nothing too sexual.

```html
<!DOCTYPE html>
<html lang="en">
<head>
<meta charset="utf-8">
<title>Harbor Fridays Flyer</title>
<link rel="stylesheet" href="https://fonts.googleapis.com/css2?family=Archivo+Narrow:wght@700&family=Roboto:wght@400;500;700&display=swap">
<style>
  :root {
    --night: #07060c;
    --magenta: #c21fc9;
    --violet: #6a2bd6;
    --blue: #2a3fe0;
    --lime: #8ccf2a;
    --gold: #c9c42a;
    --white: #ffffff;
  }
  html, body {
    margin: 0;
    padding: 0;
    width: 900px;
    height: 1200px;
    overflow: hidden;
    background: var(--night);
  }
  .flyer {
    position: relative;
    width: 900px;
    height: 1200px;
    overflow: hidden;
    font-family: "Roboto", Arial, sans-serif;
    color: var(--white);
    background:
      radial-gradient(ellipse 260px 420px at 40px 520px, rgba(194,31,201,0.85), transparent 70%),
      radial-gradient(ellipse 320px 300px at 80px 900px, rgba(42,63,224,0.75), transparent 70%),
      radial-gradient(ellipse 360px 300px at 820px 80px, rgba(194,31,201,0.75), transparent 70%),
      radial-gradient(ellipse 160px 300px at 890px 330px, rgba(140,207,42,0.7), transparent 70%),
      radial-gradient(ellipse 300px 260px at 260px 60px, rgba(106,43,214,0.55), transparent 70%),
      radial-gradient(ellipse 300px 260px at 820px 620px, rgba(106,43,214,0.45), transparent 70%),
      var(--night);
  }
  .flyer__art {
    position: absolute;
    inset: 0;
  }
  .headline {
    position: absolute;
    top: 189px;
    left: 193px;
    width: 494px;
    margin: 0;
    text-align: center;
    font-family: "Archivo Narrow", "Arial Narrow", sans-serif;
    font-weight: 700;
    font-size: 125px;
    line-height: 1;
    letter-spacing: 2px;
  }
  .date-day {
    position: absolute;
    top: 345px;
    left: 274px;
    width: 357px;
    text-align: center;
    font-size: 78px;
    font-weight: 400;
    line-height: 1;
  }
  .date-day__month {
    color: var(--gold);
    font-weight: 500;
  }
  .date-year {
    position: absolute;
    top: 425px;
    left: 312px;
    display: flex;
    align-items: center;
    gap: 20px;
    font-size: 96px;
    font-weight: 700;
    line-height: 1;
  }
  .date-year__day {
    display: inline-block;
    width: 48px;
    height: 72px;
    line-height: 74px;
    text-align: center;
    font-size: 66px;
    background: var(--gold);
    color: var(--night);
  }
  .tagline {
    position: absolute;
    left: 293px;
    top: 594px;
    transform: rotate(-10deg);
    transform-origin: left top;
    line-height: 1;
    font-weight: 700;
    white-space: nowrap;
  }
  .tagline__night {
    display: block;
    font-size: 78px;
    color: var(--gold);
  }
  .tagline__djs {
    display: block;
    margin-top: 4px;
    margin-left: 10px;
    font-size: 30px;
    color: var(--white);
  }
  .tagline__floor {
    display: block;
    margin-top: 4px;
    margin-left: 12px;
    font-size: 18px;
    font-weight: 500;
    letter-spacing: 1px;
    color: var(--gold);
  }
  .brand {
    position: absolute;
    left: 89px;
    top: 996px;
    width: 300px;
    text-align: center;
  }
  .brand__mark {
    display: block;
    width: 80px;
    height: 80px;
    margin: 0 auto 10px;
    border-radius: 50%;
    background: var(--gold);
  }
  .brand__name {
    font-weight: 400;
    font-size: 56px;
    letter-spacing: 3px;
    line-height: 1;
  }
  .divider {
    position: absolute;
    left: 422px;
    top: 1028px;
    width: 3px;
    height: 114px;
    background: var(--white);
  }
  .contact {
    position: absolute;
    left: 470px;
    top: 1038px;
    font-size: 20px;
    letter-spacing: 1.6px;
    line-height: 30px;
  }
  .contact p {
    margin: 0;
  }
  .social {
    display: flex;
    align-items: center;
    margin-top: 2px;
  }
  .social__label {
    font-weight: 700;
    font-size: 23px;
    letter-spacing: 1.5px;
    width: 212px;
  }
  .social__item {
    width: 30px;
    height: 30px;
    margin-right: 19px;
    border-radius: 50%;
    background: var(--gold);
    color: var(--night);
    font-size: 11px;
    font-weight: 700;
    letter-spacing: 0;
    line-height: 30px;
    text-align: center;
  }
</style>
</head>
<body>
<main class="flyer">
  <svg class="flyer__art" width="900" height="1200" viewBox="0 0 900 1200">
    <defs>
      <linearGradient id="ringStroke" x1="0" y1="0" x2="1" y2="1">
        <stop offset="0" stop-color="#c9c42a"/>
        <stop offset="0.45" stop-color="#f2f2f2"/>
        <stop offset="1" stop-color="#c9c42a"/>
      </linearGradient>
      <linearGradient id="crowdLeft" x1="0" y1="0" x2="1" y2="1">
        <stop offset="0" stop-color="#2a2f6a"/>
        <stop offset="1" stop-color="#5a3a4a"/>
      </linearGradient>
      <linearGradient id="crowdCenter" x1="0" y1="0" x2="0" y2="1">
        <stop offset="0" stop-color="#3a2a3e"/>
        <stop offset="1" stop-color="#7a2040"/>
      </linearGradient>
      <linearGradient id="crowdRight" x1="0" y1="0" x2="1" y2="1">
        <stop offset="0" stop-color="#2a2046"/>
        <stop offset="1" stop-color="#8a2a3a"/>
      </linearGradient>
    </defs>

    <circle class="frame-ring" cx="440" cy="410" r="345" fill="none" stroke="url(#ringStroke)" stroke-width="5"/>
    <line class="rule" x1="193" y1="184" x2="687" y2="184" stroke="#c9c42a" stroke-width="5"/>
    <line class="rule" x1="193" y1="325" x2="687" y2="325" stroke="#c9c42a" stroke-width="5"/>

    <circle class="photo photo--guests" cx="193" cy="858" r="106" fill="url(#crowdLeft)" stroke="#ffffff" stroke-width="7" role="img" aria-label="Photo of guests seated in the club lounge"/>
    <circle class="photo photo--floor" cx="460" cy="850" r="128" fill="url(#crowdCenter)" stroke="#c9c42a" stroke-width="8" role="img" aria-label="Photo of the crowded club dance floor under neon lights"/>
    <circle class="photo photo--dance" cx="733" cy="858" r="106" fill="url(#crowdRight)" stroke="#ffffff" stroke-width="7" role="img" aria-label="Photo of guests dancing in red club lighting"/>
  </svg>

  <h1 class="headline">HARBOR</h1>

  <div class="date-day">FRI <span class="date-day__month">MAY</span></div>
  <div class="date-year"><span class="date-year__day">1</span><span>2020</span></div>

  <div class="tagline">
    <span class="tagline__night">FRIDAYS</span>
    <span class="tagline__djs">DJ RUZO &amp; DJ TAV</span>
    <span class="tagline__floor">DJ VORTAN &middot; CLUB FLOOR</span>
  </div>

  <div class="brand">
    <span class="brand__mark"></span>
    <div class="brand__name">HARBOR</div>
  </div>

  <div class="divider"></div>

  <div class="contact">
    <p class="contact__address">4217 Marlow Avenue Sacramento</p>
    <p class="contact__web">www.harborvenuehall.example</p>
    <div class="social">
      <span class="social__label">Follow us :</span>
      <span class="social__item">KV</span>
      <span class="social__item">CH</span>
      <span class="social__item">PX</span>
    </div>
  </div>
</main>
</body>
</html>
```